Furniture Design Website Homepage

Brief as attached- Homepage Design

Silver Heron Furniture is a national retail emporium offering high quality, unique Scandinavian furniture, lighting and accessories. We are the market leader in this space and currently have 2 Showrooms – Melbourne & Sydney.

Most recently our business model has evolved from purely importing premium, one off vintage pieces to a more scalable model of representing brands and manufacturers exclusively out of Scandinavia. These partners manufacture today which ensures us of supply & quality.

We have now started to engage scandinavian designers and/or their families to re-introduce designs that have long gone out of production. These items are put back into production under the silver heron brand, and we own the world wide rights to them.

Please ensure you use the brief files attached and the catalogue images when creating the design.

Target Market(s)

Silver Heron Furniture - where beautiful Scandinavian design meets my modern Australian life.

We want our target audience to chose Scandinavian for their homes & for us to be their brand of choice.

The current perception is that we offer beautiful design but that it doesn’t suit everyone’s home / life / style.

Also that we are more expensive than most.

Industry/Entity Type

Retail

Requirements
Must have
• The colour scheme should be red and white as per the catalogue I attached. We like the look and feel of this site www.roomfondly.example

The furniture is more luxurious, so we need to target the upper market with a nice sleek look that makes the furniture look expensive.

```html
<!DOCTYPE html>
<html lang="en">
<head>
<meta charset="utf-8">
<title>Silver Heron Furniture – Home</title>
<link href="https://fonts.googleapis.com/css2?family=Questrial&family=Open+Sans:wght@400;600;700&display=swap" rel="stylesheet">
<style>
:root{
  --red:#e8291f;
  --red-dark:#c8100b;
  --maroon:#8b1010;
  --ink:#222;
  --text:#444;
  --muted:#666;
  --line:#d6d6d6;
  --panel:#f2f2f2;
  --page:#f7f7f7;
  --white:#fff;
  --hero-dark:#262626;
}
*{box-sizing:border-box;margin:0;padding:0}
html,body{width:1001px;height:1200px;overflow:hidden;background:var(--page)}
body{font-family:"Open Sans",Verdana,sans-serif;color:var(--text)}
.stage{position:relative;width:1200px;height:1439px;transform:scale(.83417);transform-origin:0 0;
  background:linear-gradient(#fafafa 0,#f3f3f3 160px,#f7f7f7 160px)}
.abs{position:absolute}
.heading{font-family:"Questrial",sans-serif;font-weight:400}

/* header */
.brand{left:147px;top:88px;display:flex;align-items:center;gap:10px}
.brand-mark{width:18px;height:18px;background:var(--red)}
.brand-name{font-family:"Open Sans",sans-serif;font-weight:700;font-size:31px;color:var(--ink);letter-spacing:-1px}
.tagline{left:385px;top:59px;font-size:19px;line-height:22px;color:var(--ink)}
.account{right:120px;top:33px;text-align:right;font-size:13px;color:#333;letter-spacing:.3px}
.cart{right:120px;top:66px;display:flex;align-items:center;gap:8px;font-size:13px;color:#333}
.cart a{color:#333;text-decoration:underline}
.checkout{right:120px;top:99px;background:#000;color:#fff;font-size:12px;font-weight:700;padding:2px 9px}

/* nav */
.nav{left:120px;top:135px;width:960px;height:39px;background:var(--red);border-radius:4px 4px 0 0;
  display:flex;align-items:center;padding-left:12px}
.nav a{color:#fff;text-decoration:none;font-family:"Questrial",sans-serif;font-size:15.5px;letter-spacing:.4px;
  padding:0 12px;border-right:1px solid rgba(255,255,255,.45);line-height:16px;margin-right:6px}
.nav a:last-child{border:0}

/* main panel */
.main{left:120px;top:174px;width:960px;height:1054px;background:var(--white);border-radius:0 0 10px 10px;
  box-shadow:0 8px 40px rgba(0,0,0,.07)}
.sidebar{left:120px;top:174px;width:241px;height:1054px;border-right:1px solid var(--line)}
.side-title{font-family:"Questrial",sans-serif;font-weight:400;font-size:17px;color:var(--ink)}
.search-field{left:132px;top:221px;width:214px;height:24px;border:1px solid #ccc}
.btn-red{background:var(--red-dark);color:#fff;font-family:"Questrial",sans-serif;border-radius:3px;
  border:1px solid #a00;text-align:center}
.range{left:145px;top:354px;width:193px;list-style:none;border-top:1px solid var(--line)}
.range li{height:26px;border-bottom:1px solid var(--line);font-size:13.5px;color:#333;padding:3px 0 0 8px;letter-spacing:.3px}
.range li::before{content:"→";font-size:10px;margin-right:6px;color:#555}
.filters{left:132px;top:572px;width:220px}
.filter{display:flex;align-items:center;height:26px;font-size:13.5px;color:#333;letter-spacing:.3px}
.filter span{width:88px}
.filter i{width:131px;height:22px;border:1px solid #ddd;position:relative}
.filter i::after{content:"";position:absolute;right:4px;top:8px;border:5px solid transparent;border-top-color:#ccc}
.keep{left:120px;top:802px;width:241px;height:426px;border-radius:0 0 0 10px;
  background:linear-gradient(#e9e9e9,#fafafa 35%,#f3f3f3);text-align:center}
.keep h3{font-family:"Questrial",sans-serif;font-weight:400;color:var(--maroon);font-size:20px;margin-top:24px}
.keep p{font-size:13.5px;line-height:26px;color:#333;margin-top:12px;letter-spacing:.2px}
.keep small{display:block;font-size:11px;color:var(--maroon);margin-top:12px}
.social{position:absolute;left:27px;width:186px;height:29px;background:var(--red-dark);border:1px solid #900;
  border-radius:3px;color:#fff;font-family:"Questrial",sans-serif;font-size:17px;display:flex;align-items:center;gap:10px;padding-left:8px}
.social b{width:22px;height:16px;background:#fff;border-radius:2px;opacity:.9}
.keep-brand{position:absolute;left:28px;bottom:10px;display:flex;align-items:center;gap:8px}

/* content */
.welcome{left:376px;top:192px;width:684px}
.welcome h1{font-family:"Open Sans",sans-serif;font-weight:400;font-size:18px;color:#111}
.welcome p{font-size:13.6px;line-height:18px;color:#333;margin-top:10px;letter-spacing:.45px}
.hero-photo{left:370px;top:308px;width:420px;height:296px;border-radius:4px 0 0 4px;
  background:linear-gradient(100deg,#d9d9d9,#f1f1f1 40%,#bdbab5 70%,#4a3a30)}
.hero-menu{left:790px;top:308px;width:275px;height:296px;background:linear-gradient(#3a3a3a,var(--hero-dark));border-radius:0 4px 4px 0}
.hero-menu div{height:99px;display:flex;align-items:center;padding-left:16px;color:#fff;
  font-family:"Questrial",sans-serif;font-size:25px;letter-spacing:1px;border-bottom:1px solid #555}
.hero-menu div:last-child{border:0}
.hero-menu div::before{content:"›";font-size:30px;margin-right:10px;margin-top:-4px}

.rec{left:384px;top:628px;display:flex;align-items:center;gap:12px}
.rec span{font-size:19px;color:#222}
.card{position:absolute;top:670px;width:170px;height:282px;border:1px solid #d0d0d0;background:var(--panel);text-align:center}
.card .pic{height:145px;background:var(--white);position:relative}
.card .pic div{position:absolute;left:12px;right:12px;top:14px;bottom:12px}
.card .info{position:absolute;right:6px;top:4px;width:16px;height:16px;border:1px solid #333;border-radius:50%;font-size:10px;line-height:14px;font-family:Georgia,serif;background:#fff}
.card h4{font-size:13.5px;font-weight:700;color:#111;margin-top:10px;letter-spacing:.3px}
.card .by{font-size:12px;color:#333;margin-top:5px}
.card .by em{font-style:normal;color:var(--red)}
.card .price{font-size:19px;font-weight:700;color:var(--red);margin-top:16px}
.card .add{display:inline-block;margin-top:10px;border:2px solid #333;border-radius:4px;background:#fff;
  font-size:12.5px;font-weight:600;color:#111;padding:6px 10px}

.testi-title{left:384px;top:980px;font-size:20px;color:var(--maroon)}
.quote{left:384px;top:1020px;width:329px;height:146px;border:1px solid #ccc;border-radius:3px;background:#fff;
  box-shadow:0 3px 4px rgba(0,0,0,.12);padding:14px 12px;font-size:12px;line-height:18px;color:#333}
.quote cite{display:block;text-align:right;color:var(--red-dark);font-style:normal;font-weight:700;margin-top:6px}
.news-title{left:734px;top:987px;font-size:20px;color:var(--maroon)}
.news{left:734px;top:1029px;width:330px}
.news .row{display:flex;align-items:center;justify-content:flex-end;height:38px;font-size:13.5px;color:#333;letter-spacing:.3px}
.news .row i{width:210px;height:29px;border:1px solid #ccc;margin-left:14px;position:relative}
.news .row i.sel::after{content:"";position:absolute;right:5px;top:11px;border:5px solid transparent;border-top-color:#bbb}

/* footer */
.footer{left:120px;top:1242px;width:960px;height:178px;background:#eee;border:1px solid #ccc;border-radius:4px;font-family:Arial,Helvetica,sans-serif}
.fcol{position:absolute;top:10px;font-size:12px;color:#555;line-height:22.5px}
.fcol b{color:#444;font-weight:700}
.pay{position:absolute;width:58px;height:32px;border-radius:3px;background:#fff;border:1px solid #ddd}
.seal{position:absolute;left:727px;top:45px;width:64px;height:64px;border-radius:50%;background:#d9b23a}
.rights{position:absolute;right:23px;top:150px;font-size:12px;color:#555}
</style>
</head>
<body>
<div class="stage">

  <header>
    <div class="abs brand"><span class="brand-mark"></span><span class="brand-name">silver heron</span></div>
    <p class="abs tagline heading">The Best of Modern and Classic<br>Skandinavian Design</p>
    <div class="abs account">LOGIN / REGISTER</div>
    <div class="abs cart">
      <svg width="28" height="24" viewBox="0 0 28 24" aria-hidden="true"><path d="M1 2h4l3 13h15l3-10H7" fill="none" stroke="#111" stroke-width="2"/><circle cx="10" cy="20" r="2" fill="#111"/><circle cx="21" cy="20" r="2" fill="#111"/></svg>
      <a>5 items $4500</a>
    </div>
    <div class="abs checkout">Checkout ▸</div>
  </header>

  <nav class="abs nav">
    <a>ABOUT US</a><a>FURNITURE RESTORATION</a><a>MEDIA</a><a>FAQ</a><a>MAILING LIST</a><a>BLOG</a><a>SITE SEARCH</a><a>CONTACT US</a>
  </nav>

  <main class="abs main"></main>
  <aside class="abs sidebar"></aside>

  <h2 class="abs side-title" style="left:133px;top:193px">Product Search</h2>
  <div class="abs search-field">
    <svg class="abs" style="right:4px;top:4px" width="16" height="16" viewBox="0 0 16 16" aria-hidden="true"><circle cx="6" cy="6" r="4.5" fill="none" stroke="#bbb" stroke-width="1.5"/><path d="M9.5 9.5l5 5" stroke="#bbb" stroke-width="2"/></svg>
  </div>
  <div class="abs btn-red" style="left:268px;top:263px;width:78px;height:28px;font-size:16px;line-height:26px">Search</div>

  <h2 class="abs side-title" style="left:133px;top:324px">Browse Our Range</h2>
  <ul class="abs range">
    <li>Furniture</li><li>Furniture Packages</li><li>Accessories</li><li>Lighting</li><li>Fabrics</li>
  </ul>

  <h2 class="abs side-title" style="left:133px;top:535px">View Product by Type</h2>
  <div class="abs filters">
    <div class="filter"><span>Room:</span><i></i></div>
    <div class="filter"><span>Furniture:</span><i></i></div>
    <div class="filter"><span>Designer:</span><i></i></div>
    <div class="filter"><span>Brand:</span><i></i></div>
    <div class="filter"><span>Accessories:</span><i></i></div>
  </div>
  <div class="abs btn-red" style="left:240px;top:721px;width:112px;height:28px;font-size:17px;line-height:26px">Find Product</div>

  <section class="abs keep">
    <h3>Keep Up to Date</h3>
    <p>Discover exclusive offers,<br>product previews and<br>much more!</p>
    <small>We value your privacy.</small>
    <div class="social" style="top:190px"><b></b>Our Newsletter</div>
    <div class="social" style="top:233px"><b></b>Our Facepage</div>
    <div class="social" style="top:275px"><b></b>Our Chirper</div>
    <div class="keep-brand"><span class="brand-mark"></span><span class="brand-name">silver heron</span></div>
  </section>

  <section class="abs welcome">
    <h1>Welcome to Silver Heron!</h1>
    <p>Lorem ipsum dolor sit amet, consectetur adipiscing elit. Integer et nunc erat, at luctus purus. Vivamus nec ipsum sit amet elit rutrum ultrices pretium ut massa. In at mauris at massa gravida condimentum. Sed quis nisi a nunc scelerisque varius. Aenean sodales nibh ac lorem varius at inter-dum massa hendrerit.</p>
  </section>

  <div class="abs hero-photo" role="img" aria-label="Photo of a child resting in a white lounge chair in a modern living room"></div>
  <div class="abs hero-menu"><div>FURNITURE</div><div>ACCESSORIES</div><div>LIGHTING</div></div>

  <div class="abs rec"><span class="brand-name" style="font-size:26px">silver heron</span><span>recommends:</span></div>

  <article class="card" style="left:375px">
    <div class="pic"><div role="img" aria-label="Grey upholstered two-seat sofa" style="background:linear-gradient(#5a5a5e,#333)"></div><span class="info">i</span></div>
    <h4>Model 38</h4><p class="by">by <em>Nordvik Studio</em></p><p class="price">$2,229</p><span class="add">Add to Cart</span>
  </article>
  <article class="card" style="left:549px">
    <div class="pic"><div role="img" aria-label="Green rocking lounge chair" style="background:linear-gradient(#a6d24a,#79a82a)"></div><span class="info">i</span></div>
    <h4>Skate Chair</h4><p class="by">by <em>Lunde Møbler</em></p><p class="price">$2,229</p><span class="add">Add to Cart</span>
  </article>
  <article class="card" style="left:723px">
    <div class="pic"><div role="img" aria-label="Wooden chest of drawers" style="background:linear-gradient(#fff 25%,#8a5a3c 25%,#6b4027 75%,#fff 75%)"></div><span class="info">i</span></div>
    <h4>Tilde Chest of drawers</h4><p class="by">by <em>Silver Heron Denmark</em></p><p class="price">$2,229</p><span class="add">Add to Cart</span>
  </article>
  <article class="card" style="left:897px">
    <div class="pic"><div role="img" aria-label="Chrome table lamp" style="background:radial-gradient(circle at 40% 35%,#eee,#999 45%,#fff 70%)"></div><span class="info">i</span></div>
    <h4>Bellflower - Table BL2</h4><p class="by">by <em>Nordvik Studio</em></p><p class="price">$2,229</p><span class="add">Add to Cart</span>
  </article>

  <h3 class="abs heading testi-title">Testimonials</h3>
  <blockquote class="abs quote">Lorem ipsum dolor sit amet, consectetur adipiscing elit. Nunc in lorem arcu, sit amet interdum purus. Duis non tellus enim, at mollis odio. In interdum dictum lectus, elementum ultricies massa ullamcor-per nec. Praesent a mattis lorem.<cite>Jane Porter, Hobart</cite></blockquote>
  <svg class="abs" style="left:610px;top:1164px" width="64" height="48" viewBox="0 0 64 48" aria-hidden="true"><path d="M0 1h64L8 46z" fill="#fff" stroke="#ccc"/><path d="M0 0h64" stroke="#fff" stroke-width="3"/></svg>

  <h3 class="abs heading news-title">Join Our Newsletter</h3>
  <form class="abs news">
    <div class="row">Your name:<i></i></div>
    <div class="row">Your e-mail:<i></i></div>
    <div class="row">State:<i class="sel"></i></div>
    <div class="row">Postcode:<i></i></div>
  </form>
  <div class="abs btn-red" style="left:878px;top:1184px;width:186px;height:29px;font-size:17px;line-height:27px">Join Our Newsletter</div>

  <footer class="abs footer">
    <div class="fcol" style="left:29px"><b>Our company</b><br>About Us<br>Shop Locator<br>Contact Us<br>Sitemap<br>Terms of Use<br>Privacy Policy</div>
    <div class="fcol" style="left:192px"><b>Shopping Information</b><br>Worldwide Delivery<br>General Sales Conditions<br>Return policy<br>Gift order<br>Secure payment<br>Help</div>
    <div class="fcol" style="left:395px"><b>Your Account</b><br>Sign In<br>Your personnal details<br>Follow up your order<br>Sign up to our newsletter</div>
    <div class="seal"></div>
    <span class="pay" style="left:813px;top:15px"></span><span class="pay" style="left:884px;top:15px"></span>
    <span class="pay" style="left:813px;top:59px"></span><span class="pay" style="left:884px;top:59px"></span>
    <span class="pay" style="left:813px;top:103px"></span><span class="pay" style="left:884px;top:103px"></span>
    <p class="rights">All rights reserved © 2011 Silver Heron</p>
  </footer>

</div>
</body>
</html>
```